Branding Package for an environmental water treatment operations company
Use the provided Logo. The name of the company is Coordinated Ecological Solutions or CES
Branding Package for an environmental water treatment operations company - Environment
Creative Brief
Professional
Mark Delane
President
217 Thornbury Ave Canonsburg, PA. 15317
tkvallen@mailbrook.net
U have freedom to experiment with any fonts to find the best match.
I will add to this later as I see what's being submitted.

```html
<!DOCTYPE html>
<html lang="en">
<head>
<meta charset="utf-8">
<title>Coordinated Ecological Solutions Business Card</title>
<link rel="stylesheet" href="https://fonts.googleapis.com/css2?family=Open+Sans:wght@400;600;700&display=swap">
<style>
  :root {
    --page-bg: #ecebe8;
    --brand-blue: #1f3fa6;
    --brand-blue-deep: #14287a;
    --brand-blue-light: #3a63d6;
    --accent-green: #7cc242;
    --accent-yellow: #d8e03a;
    --card-white: #ffffff;
    --text-white: #ffffff;
    --text-blue: #1f3fa6;
  }
  * { box-sizing: border-box; margin: 0; padding: 0; }
  html, body {
    width: 1200px;
    height: 799px;
    overflow: hidden;
    background: var(--page-bg);
    font-family: "Open Sans", Arial, sans-serif;
  }
  .canvas {
    position: relative;
    width: 1200px;
    height: 799px;
  }
  .card {
    position: absolute;
    top: 256px;
    width: 500px;
    height: 286px;
    border-radius: 22px;
    overflow: hidden;
    box-shadow: 0 14px 30px rgba(0,0,0,0.18);
  }
  .card-front {
    left: 70px;
    background: radial-gradient(ellipse at 40% 45%, var(--brand-blue-light) 0%, var(--brand-blue) 45%, var(--brand-blue-deep) 100%);
  }
  .card-back {
    left: 630px;
    background: var(--card-white);
  }
  .card-back .wave {
    position: absolute;
    inset: 0;
    width: 100%;
    height: 100%;
  }
  .brand {
    position: absolute;
    display: flex;
    align-items: center;
    gap: 12px;
  }
  .brand-dot {
    flex: none;
    width: 30px;
    height: 30px;
    border-radius: 50%;
    background: var(--accent-green);
  }
  .brand-name {
    font-size: 19px;
    font-weight: 600;
    line-height: 1.25;
    width: 190px;
  }
  .card-front .brand { left: 140px; top: 116px; }
  .card-front .brand-name { color: var(--text-white); }

  .card-back .brand { left: 30px; top: 176px; }
  .card-back .brand-name { color: var(--text-blue); }

  .contact {
    position: absolute;
    right: 30px;
    top: 28px;
    text-align: right;
    color: var(--text-white);
  }
  .contact-name {
    font-size: 17px;
    font-weight: 700;
  }
  .contact-title {
    font-size: 11px;
    font-weight: 400;
    margin-bottom: 30px;
  }
  .contact-list {
    list-style: none;
    font-size: 10px;
    line-height: 1.55;
  }
  .contact-list li {
    display: flex;
    justify-content: flex-end;
    align-items: center;
    gap: 8px;
  }
  .contact-list li::after {
    content: "";
    width: 9px;
    height: 9px;
    border-radius: 50%;
    background: var(--text-white);
  }
</style>
</head>
<body>
<main class="canvas">
  <section class="card card-front" aria-label="Card front">
    <div class="brand">
      <span class="brand-dot"></span>
      <span class="brand-name">Coordinated Ecological Solutions</span>
    </div>
  </section>

  <section class="card card-back" aria-label="Card back">
    <svg class="wave" viewBox="0 0 500 286" preserveAspectRatio="none" aria-hidden="true">
      <defs>
        <linearGradient id="back-blue" x1="0" y1="0" x2="1" y2="1">
          <stop offset="0" stop-color="#3a63d6"/>
          <stop offset="1" stop-color="#14287a"/>
        </linearGradient>
      </defs>
      <path d="M0,0 H500 V286 H330 C300,200 240,150 150,130 C80,115 30,120 0,130 Z" fill="url(#back-blue)"/>
      <path d="M0,136 C30,126 80,121 150,136 C240,156 296,206 322,286" fill="none" stroke="var(--accent-green)" stroke-width="5"/>
      <path d="M0,142 C30,132 80,128 150,142 C236,162 290,210 314,286" fill="none" stroke="var(--accent-yellow)" stroke-width="2"/>
    </svg>
    <div class="brand">
      <span class="brand-dot"></span>
      <span class="brand-name">Coordinated Ecological Solutions</span>
    </div>
    <div class="contact">
      <p class="contact-name">Mark Delane</p>
      <p class="contact-title">President</p>
      <ul class="contact-list">
        <li>217 Thornbury Ave</li>
        <li>Harlow Ridge, PA. 15482</li>
        <li>(724) 555-0142</li>
        <li>(724) 555-0187</li>
        <li>tkvallen@mailbrook.net</li>
        <li>www.cesolutions.net</li>
      </ul>
    </div>
  </section>
</main>
</body>
</html>
```